Pamphlet for IT Services Company (MSP Provider or Managed Services Provider)

We need a pamphlet designed for our Managed Services Company. We are an established company of 17 years that has never advertised. We'd like a pamphlet that we can drop off at potential client sites that describes our services. I like clean and prefer Orange as an accent color. We'd like to touch on the fact that we cater to our clients needs and go above and beyond what the other providers do.

Target Market(s)

Small and Medium Sized Businesses

Industry/Entity Type

It Service

Font styles to use
Other font styles liked:
• Try to match font on logo or website

Requirements
Must have
• Must highlight with the following Services and descriptions with Logo
Managed IT Services
IT Support
VOIP Solutions
WiFI Solutions
Contact information with phone number and website address.
Please view website korvanetpro.com
try to match fons on website above.
Nice to have
• Customer Testimonials. May a couple one line testimonials. Not real sure because this is the first time we've ever designed a brochure.
Should not have
• Not Sure

```html
<!DOCTYPE html>
<html lang="en">
<head>
<meta charset="utf-8">
<title>Korvanet Pro – Managed IT Services</title>
<link rel="stylesheet" href="https://fonts.googleapis.com/css2?family=Fira+Sans:wght@400;500;600&family=Source+Sans+3:wght@400;600&family=Raleway:wght@400&display=swap">
<style>
  :root {
    --orange: #f5892c;
    --slate: #647a8f;
    --cream: #fdf8f1;
    --navy: #1f2b3a;
    --ink: #2b2b2b;
    --white: #ffffff;
    --page-bg: #e9e7e4;
  }
  * { box-sizing: border-box; margin: 0; padding: 0; }
  html, body { width: 1200px; height: 801px; overflow: hidden; background: var(--page-bg); }
  .flyer {
    position: absolute; left: 294px; top: 4px; width: 612px; height: 793px;
    background: var(--white); font-family: "Source Sans 3", Arial, sans-serif; color: var(--ink);
    box-shadow: 0 4px 14px rgba(0,0,0,.18); overflow: hidden;
  }
  .hero-photo {
    position: absolute; left: 0; top: 60px; width: 612px; height: 322px;
    background: linear-gradient(120deg, #2c3d52 0%, #4a5a6c 40%, #6c6a66 70%, #8a6a4c 100%);
  }
  .hero-photo::after {
    content: ""; position: absolute; inset: 0;
    background: linear-gradient(180deg, rgba(0,0,0,0) 55%, rgba(20,25,35,.45) 100%);
  }
  .header-cut { position: absolute; left: 0; top: 0; width: 612px; height: 112px; }
  .brand {
    position: absolute; left: 22px; top: 46px;
    font-family: "Raleway", Arial, sans-serif; font-weight: 400; font-size: 25px; color: var(--orange);
    display: flex; align-items: center; gap: 8px;
  }
  .brand-dot { width: 12px; height: 12px; border-radius: 50%; background: var(--orange); }
  .tagline {
    position: absolute; right: 26px; top: 39px; font-size: 10.5px; font-weight: 600; color: #222;
  }
  .hero-title {
    position: absolute; left: 0; width: 612px; top: 168px; text-align: center; color: var(--white);
    font-family: "Fira Sans", Arial, sans-serif; font-weight: 500; font-size: 26px; padding-left: 105px;
    text-shadow: 0 1px 3px rgba(0,0,0,.4);
  }
  .hero-sub {
    position: absolute; left: 0; width: 612px; top: 207px; text-align: center; color: var(--white);
    font-size: 12.5px; padding-left: 106px; text-shadow: 0 1px 2px rgba(0,0,0,.4);
  }
  .services { position: absolute; top: 393px; left: 0; width: 612px; height: 259px; display: flex; }
  .service { width: 153px; height: 100%; text-align: center; padding: 38px 10px 0; }
  .service svg { width: 36px; height: 40px; }
  .service h3 {
    font-family: "Fira Sans", Arial, sans-serif; font-weight: 500; font-size: 13px; margin-top: 18px;
  }
  .service .lead { font-size: 8px; opacity: .75; margin-top: 3px; }
  .service p { font-size: 9px; line-height: 12px; margin-top: 17px; }
  .service h3 + p { margin-top: 29px; }
  .service--managed { background: var(--slate); color: var(--white); }
  .service--support { background: var(--cream); color: #333; }
  .service--support h3 { color: var(--orange); }
  .service--voip { background: var(--orange); color: var(--white); }
  .service--wifi { background: var(--navy); color: var(--white); }
  .partners {
    position: absolute; top: 670px; left: 18px; width: 580px; height: 56px;
    display: flex; align-items: center; justify-content: space-between;
  }
  .partner { background: #d9dde2; }
  .partner--wide { width: 100px; height: 16px; border-radius: 3px; }
  .partner--badge { width: 92px; height: 30px; background: #5c5f63; }
  .partner--small { width: 30px; height: 30px; border-radius: 50%; background: #6a5a9a; }
  .partner--box { width: 50px; height: 50px; border: 1px solid #cfd3d8; background: #f4f6f8; }
  .contact-bar {
    position: absolute; top: 752px; left: 0; width: 612px; height: 26px; background: var(--orange);
    display: flex; align-items: center; justify-content: space-between; padding: 0 18px 0 24px;
    color: var(--white); font-family: "Fira Sans", Arial, sans-serif; font-size: 11.5px; letter-spacing: .3px;
  }
  .contact-item { display: flex; align-items: center; gap: 8px; }
  .contact-icon { width: 14px; height: 14px; background: var(--white); border-radius: 3px; display: flex; align-items: center; justify-content: center; }
</style>
</head>
<body>
<main class="flyer">
  <div class="hero-photo" role="img" aria-label="Photo of an open laptop showing an analytics dashboard in an office"></div>
  <svg class="header-cut" viewBox="0 0 612 112" aria-hidden="true">
    <polygon points="0,0 612,0 612,60 335,60 300,110 0,110" fill="#ffffff"/>
  </svg>
  <div class="brand"><span class="brand-dot"></span>korvanet pro</div>
  <div class="tagline">"Wouldn't it be nice if your stuff just worked?"</div>
  <h1 class="hero-title">Managed IT Services</h1>
  <div class="hero-sub">A Simple, Cost Effective Plan for your IT Infrastructure.</div>

  <section class="services">
    <article class="service service--managed">
      <svg viewBox="0 0 36 40" aria-hidden="true"><path d="M3 3h30v17c0 9-8 15-15 18C11 35 3 29 3 20z" fill="#fff"/><path d="M18 8h10v12c0 6-5 10-10 12z" fill="#647a8f"/></svg>
      <h3>Managed IT Services</h3>
      <div class="lead">Let us take care of your IT</div>
      <p>Our MSP is a Flat Rate service that includes Onsite &amp; Remote Support, Endpoint Protection, Web Filtering, Encrypted Online Backup &amp; Patch Management</p>
    </article>
    <article class="service service--support">
      <svg viewBox="0 0 36 40" aria-hidden="true" fill="none" stroke="#1f2b3a" stroke-width="3"><circle cx="18" cy="12" r="8"/><path d="M5 37v-5c0-6 5-10 13-10s13 4 13 10v5z"/></svg>
      <h3>IT Support</h3>
      <p>We have a passion for what we do and it shows! Korvanet provides fast, reliable, expert solutions from experienced staff. You will never feel like just another client to us because our customers are family!</p>
    </article>
    <article class="service service--voip">
      <svg viewBox="0 0 36 40" aria-hidden="true"><path d="M9 8c3-2 5 0 6 3s1 4-1 5c-1 1 1 6 4 8 2 1 3-1 5 0s3 3 1 6c-2 3-6 3-10 0S4 19 5 13c0-2 2-4 4-5z" fill="#1f2b3a"/><path d="M22 6a7 7 0 0 1 6 7M24 1a12 12 0 0 1 10 11" stroke="#1f2b3a" stroke-width="2.5" fill="none"/></svg>
      <h3>VOIP Solutions</h3>
      <p>Phones are more than just an attachment to a desk. Allow us to help you maximize communication with your team and customers by using the latest technology that will likely save you money as well. Korvanet Pro partners with Lineway to provide phone</p>
    </article>
    <article class="service service--wifi">
      <svg viewBox="0 0 36 40" aria-hidden="true" fill="none" stroke="#fff" stroke-width="3.5" stroke-linecap="round"><path d="M3 16a22 22 0 0 1 30 0"/><path d="M9 22a13 13 0 0 1 18 0"/><circle cx="18" cy="29" r="2.5" fill="#fff" stroke="none"/></svg>
      <h3>WiFi Solutions</h3>
      <p>WiFi is everywhere! (At least it should be.) Korvanet can extend your WiFi to cover your whole campus.</p>
    </article>
  </section>

  <section class="partners" aria-label="Technology partners">
    <span class="partner partner--wide"></span>
    <span class="partner partner--wide"></span>
    <span class="partner partner--badge"></span>
    <span class="partner partner--small"></span>
    <span class="partner partner--wide"></span>
    <span class="partner partner--box"></span>
  </section>

  <footer class="contact-bar">
    <span class="contact-item"><span class="contact-icon"><svg width="10" height="8" viewBox="0 0 10 8"><rect x=".5" y=".5" width="9" height="7" fill="none" stroke="#f5892c"/><path d="M.5 .5l4.5 4 4.5-4" fill="none" stroke="#f5892c"/></svg></span>jmarlow@korvanetpro.com</span>
    <span class="contact-item"><span class="contact-icon"><svg width="9" height="9" viewBox="0 0 10 10"><path d="M2 1c1 0 2 2 2 2L3 4c1 2 2 3 3 3l1-1s2 1 2 2-1 2-2 2C4 10 0 6 0 3 0 2 1 1 2 1z" fill="#f5892c"/></svg></span>+1 (555) 014-2287</span>
    <span class="contact-item"><span class="contact-icon"><svg width="10" height="10" viewBox="0 0 10 10"><circle cx="5" cy="5" r="4" fill="none" stroke="#f5892c"/><path d="M1 5h8M5 1c2 2 2 6 0 8M5 1c-2 2-2 6 0 8" fill="none" stroke="#f5892c" stroke-width=".8"/></svg></span>www.korvanetpro.com</span>
  </footer>
</main>
</body>
</html>
```